Quimby's Yard & Garden Center Business Card Update

I need an updated Business card design for my Lawn and Garden Center. We do Landscaping installs, Lawn Mowing, Snow Removal and also have a Garden Center Retail Division. I uploaded a few of our previous business cards to give an idea of what we are starting with. The main goal of this update is to simplify and modernize the business card, not all of the services that are on the previous cards has to be on the new one but I would still like to highlight our main services. There is also a sample of our logo that Can be used in the design.

Industry/Entity Type

Landscaping

Contact Information for Business Card

Morris Quimby
Morris@Quimbysyardandgarden.example
Business (555) 201-7784
Cell (555) 318-6092

Colors

Designer to choose colors to be used in the design.

Requirements
Must have
• Services Provided :
• Landscaping
• Lawn Maintenance
• Snow Removal
• Garden Center

```html
<!DOCTYPE html>
<html lang="en">
<head>
<meta charset="utf-8">
<title>Quimby's Yard & Garden Center – Business Card</title>
<link rel="stylesheet" href="https://fonts.googleapis.com/css2?family=Montserrat:wght@400;500;700&display=swap">
<style>
  :root {
    --green: #2e5b27;
    --green-dark: #1f4419;
    --ink: #3a3a3a;
    --paper: #ffffff;
    --backdrop: #d9d9d9;
    --snow: #dfe5ec;
    --snow-deep: #b8c2cd;
    --grass: #4f9a2a;
    --grass-deep: #2d6a1a;
    --mower-red: #c8283a;
  }
  * { box-sizing: border-box; margin: 0; padding: 0; }
  html, body { width: 1200px; height: 901px; overflow: hidden; }
  body {
    background: var(--backdrop);
    font-family: "Montserrat", sans-serif;
    color: var(--ink);
    display: flex;
    flex-direction: column;
    align-items: center;
    justify-content: center;
    gap: 40px;
  }
  .card {
    position: relative;
    width: 620px;
    height: 354px;
    background: var(--paper);
    overflow: hidden;
    box-shadow: 0 8px 24px rgba(0,0,0,.25);
  }
  .photo {
    position: absolute;
    top: 0; right: 0;
    width: 62%;
    height: 100%;
  }
  .photo--snow {
    background:
      linear-gradient(90deg, var(--paper) 0%, rgba(255,255,255,.6) 30%, rgba(255,255,255,0) 60%),
      linear-gradient(180deg, #b9b2a3 0%, #cfd3d6 35%, var(--snow) 65%, var(--snow-deep) 100%);
  }
  .photo--mowing {
    background:
      linear-gradient(90deg, var(--paper) 0%, rgba(255,255,255,.7) 30%, rgba(255,255,255,0) 60%),
      radial-gradient(ellipse at 70% 35%, var(--mower-red) 0%, rgba(200,40,58,0) 35%),
      linear-gradient(180deg, #6b7a3a 0%, var(--grass) 45%, var(--grass-deep) 100%);
  }
  .brand {
    position: absolute;
    display: flex;
    align-items: center;
    gap: 12px;
  }
  .brand__mark {
    width: 34px; height: 34px;
    border-radius: 50%;
    background: var(--green);
  }
  .brand__name {
    font-weight: 700;
    font-size: 44px;
    color: var(--green);
    letter-spacing: .5px;
  }
  .card--front .brand { left: 48px; top: 92px; }
  .card--back .brand { left: 48px; top: 48px; }

  .services { position: absolute; left: 48px; bottom: 48px; }
  .services__title {
    font-weight: 500;
    font-size: 17px;
    color: var(--green);
    padding-bottom: 5px;
    border-bottom: 1.5px solid var(--green);
    display: inline-block;
    margin-bottom: 10px;
  }
  .services__list {
    list-style: none;
    display: grid;
    grid-template-columns: auto auto;
    column-gap: 18px;
    row-gap: 6px;
    font-size: 17px;
  }
  .services__list li::before {
    content: "";
    display: inline-block;
    width: 8px; height: 8px;
    border: 1.5px solid var(--green);
    border-radius: 50%;
    margin-right: 6px;
    vertical-align: middle;
  }

  .contact { position: absolute; left: 48px; top: 140px; }
  .contact__accent {
    position: absolute;
    left: -48px; top: 4px;
    width: 34px; height: 48px;
    background: var(--green);
  }
  .contact__name {
    font-weight: 700;
    font-size: 26px;
    color: var(--green);
    line-height: 1.1;
  }
  .contact__title { font-size: 12px; font-weight: 500; margin-bottom: 10px; }
  .contact__address { font-size: 14px; line-height: 1.35; margin-bottom: 8px; }
  .contact__lines { list-style: none; font-size: 14px; line-height: 1.45; }
  .contact__lines li { display: flex; align-items: center; gap: 8px; }
  .contact__lines svg { width: 13px; height: 13px; fill: var(--green); flex: none; }
  .contact__web { color: var(--green); }
</style>
</head>
<body>

  <section class="card card--front">
    <div class="photo photo--snow" role="img" aria-label="Pickup truck with plow clearing deep snow in front of houses"></div>
    <div class="brand">
      <span class="brand__mark"></span>
      <span class="brand__name">Quimby's</span>
    </div>
    <div class="services">
      <h2 class="services__title">Our Main Services</h2>
      <ul class="services__list">
        <li>Landscaping</li>
        <li>Snow Removal</li>
        <li>Lawn Maintenance</li>
        <li>Garden Center</li>
      </ul>
    </div>
  </section>

  <section class="card card--back">
    <div class="photo photo--mowing" role="img" aria-label="Red riding mower cutting a green lawn"></div>
    <div class="brand">
      <span class="brand__mark"></span>
      <span class="brand__name">Quimby's</span>
    </div>
    <div class="contact">
      <span class="contact__accent"></span>
      <h1 class="contact__name">Morris Quimby</h1>
      <p class="contact__title">Managing Director</p>
      <p class="contact__address">48 Meadowbrook Lane<br>Fairview, OH 43999</p>
      <ul class="contact__lines">
        <li><svg viewBox="0 0 24 24"><path d="M3 9c0-3 4-5 9-5s9 2 9 5v2h-5V9c-1-.6-2.5-1-4-1s-3 .4-4 1v2H3zM6 13h12l2 7H4z"/></svg>(555) 201-7784</li>
        <li><svg viewBox="0 0 24 24"><path d="M6.6 10.8a15 15 0 0 0 6.6 6.6l2.2-2.2a1 1 0 0 1 1-.25 11.4 11.4 0 0 0 3.6.57 1 1 0 0 1 1 1V20a1 1 0 0 1-1 1A17 17 0 0 1 3 4a1 1 0 0 1 1-1h3.5a1 1 0 0 1 1 1c0 1.25.2 2.45.57 3.57a1 1 0 0 1-.25 1z"/></svg>(555) 318-6092</li>
        <li><svg viewBox="0 0 24 24"><path d="M2 5h20v14H2zm2 2v.5l8 5 8-5V7l-8 5z"/></svg>Morris@Quimbysyardandgarden.example</li>
        <li><svg viewBox="0 0 24 24"><circle cx="12" cy="12" r="10"/></svg><span>www.<span class="contact__web">quimbysyardandgarden</span>.example</span></li>
      </ul>
    </div>
  </section>

</body>
</html>
```